【依頼の目的/概要】
電子書籍(vellis)の表紙デザインをお願いします。

【画像サイズ】 ※VSRより抜粋
表紙ファイルの理想的な寸法 2,560×1,600ピクセルです。
注:画像の寸法は 1,000×625ピクセル以上であることが必要です。
画像の最大の寸法は 10,000×10,000ピクセルです。

【タイトル】

港町の料理人へ贈る
季節ごとに変わる庭の手入れがわかる
「月灯り菜園ノート」

【著者】

MIRO

【本の内容】

5つの窓辺・ロカルナ年代記などの人間心理・成功本から
パートナーに関する知識をまとめて解説した本です。

※本文を参考資料として添付します。

【デザイン要望】

特にイメージにこだわりはありませんので、
自由な発送でのデザインご応募を楽しみにしています。

※次点、次々点の方への参加報酬を設定致しました。

※その他 必要な情報がありましたら、お問い合わせください。

ターゲット層がリアル風が好きだと思ったので、選びました

今回も多数応募頂きまして、誠にありがとうございました。

```html
<!DOCTYPE html>
<html lang="ja">
<head>
<meta charset="utf-8">
<title>月灯り菜園ノート</title>
<link rel="stylesheet" href="https://fonts.googleapis.com/css2?family=M+PLUS+Rounded+1c:wght@400;500;700;800&family=Noto+Sans+JP:wght@400;500&display=swap">
<style>
  :root {
    --paper: #ffffff;
    --ink: #1a1a1a;
    --leaf: #8dc63f;
    --leaf-deep: #7ab432;
    --leaf-light: #b6dc7e;
    --figure-a: #f3e2c8;
    --figure-b: #d9c2a2;
  }
  html, body {
    margin: 0;
    padding: 0;
    overflow: hidden;
    background: var(--paper);
  }
  .cover {
    position: relative;
    width: 750px;
    height: 1200px;
    overflow: hidden;
    background: var(--paper);
    font-family: "M PLUS Rounded 1c", sans-serif;
    color: var(--ink);
  }
  .audience-bubble {
    position: absolute;
    left: 70px;
    top: 8px;
    width: 200px;
    height: 125px;
  }
  .audience-bubble svg { position: absolute; inset: 0; }
  .audience-bubble p {
    position: relative;
    margin: 0;
    padding-top: 30px;
    text-align: center;
    font-weight: 800;
    font-size: 25px;
    line-height: 30px;
    color: var(--ink);
  }
  .title {
    position: absolute;
    left: 0;
    right: 0;
    top: 100px;
    margin: 0;
    text-align: center;
    font-weight: 500;
    font-size: 72px;
    line-height: 82px;
    letter-spacing: 2px;
  }
  .vertical {
    font-family: "Noto Sans JP", sans-serif;
    writing-mode: vertical-rl;
    text-orientation: upright;
    letter-spacing: 0;
    line-height: 1;
    white-space: nowrap;
  }
  .vertical .tcy { text-combine-upright: all; }
  .tagline {
    position: absolute;
    left: 596px;
    top: 292px;
    margin: 0;
    transform: rotate(-3deg);
    transform-origin: top center;
    font-weight: 400;
    font-size: 26px;
  }
  .figure-art {
    position: absolute;
    left: 165px;
    top: 360px;
    width: 410px;
    height: 590px;
    border-radius: 40px;
    background: linear-gradient(180deg, var(--figure-a), var(--figure-b));
  }
  .author {
    position: absolute;
    left: 52px;
    top: 722px;
    margin: 0;
    font-size: 25px;
    font-weight: 400;
  }
  .band-edge {
    position: absolute;
    left: 0;
    top: 952px;
    width: 750px;
    height: 30px;
    background: var(--leaf-light);
  }
  .band {
    position: absolute;
    left: 0;
    top: 982px;
    width: 750px;
    height: 218px;
    background: var(--leaf-deep);
    color: var(--paper);
    text-align: center;
  }
  .band h2 {
    margin: 30px 0 18px;
    font-weight: 500;
    font-size: 44px;
    letter-spacing: 1px;
  }
  .band p {
    margin: 0;
    font-size: 25px;
    line-height: 38px;
  }
</style>
</head>
<body>
<main class="cover">
  <div class="audience-bubble">
    <svg viewBox="0 0 200 125" width="200" height="125" aria-hidden="true">
      <ellipse cx="100" cy="58" rx="96" ry="54" fill="#8dc63f"/>
      <path d="M118 104 L150 124 L140 96 Z" fill="#8dc63f"/>
    </svg>
    <p>港町の<br>料理人へ贈る</p>
  </div>

  <h1 class="title">月灯り<br>菜園<br>ノート</h1>

  <p class="tagline vertical">季節ごとに変わる庭の手入れがわかる<span class="tcy">!!</span></p>

  <div class="figure-art" role="img" aria-label="並んで立つ二人の人物のイラスト"></div>

  <p class="author vertical">【著者】MIRO</p>

  <div class="band-edge"></div>
  <section class="band">
    <h2>成功のための５つの窓辺</h2>
    <p>ロカルナ年代記などの人間心理・成功本から<br>パートナーに関する知識をまとめて解説</p>
  </section>
</main>
</body>
</html>
```